The Hidden Roots of Lingering Illness Decoded

Subtitle: At last, uncover what drives your aches, exhaustion, and swelling.

I need an awesome book cover that fits this title.

```html
<!DOCTYPE html>
<html lang="en">
<head>
<meta charset="utf-8">
<title>The Hidden Roots of Lingering Illness Decoded – Book Cover</title>
<link rel="stylesheet" href="https://fonts.googleapis.com/css2?family=Montserrat:wght@800;900&family=Open+Sans:wght@700&display=swap">
<style>
  :root {
    --backdrop: #9e9d9e;
    --paper: #ffffff;
    --ink: #161616;
    --title-blue: #1172be;
    --title-red: #d0003a;
    --accent-red: #c8101e;
    --band-red: #d0003a;
    --band-text: #ffffff;
    --rule: #2a2a2a;
  }
  * { margin: 0; padding: 0; box-sizing: border-box; }
  html, body {
    width: 1200px;
    height: 1200px;
    overflow: hidden;
    background: var(--backdrop);
  }
  .book-cover {
    position: absolute;
    left: 293px;
    top: 140px;
    width: 614px;
    height: 920px;
    background: var(--paper);
  }
  .cover-title {
    position: absolute;
    left: 0;
    top: 0;
    width: 614px;
    height: 330px;
  }
  .cover-title text {
    font-family: "Montserrat", sans-serif;
    font-weight: 900;
  }
  .title-lead { fill: var(--ink); font-weight: 800; }
  .title-blue { fill: var(--title-blue); }
  .title-red { fill: var(--title-red); }
  .title-rule { stroke: var(--rule); stroke-width: 1.5; }
  .cover-subtitle {
    position: absolute;
    left: 20px;
    top: 385px;
    width: 574px;
    text-align: center;
    font-family: "Open Sans", sans-serif;
    font-weight: 700;
    font-size: 27px;
    line-height: 31px;
    color: var(--ink);
    letter-spacing: 0.5px;
    text-transform: uppercase;
  }
  .cover-subtitle .highlight { color: var(--accent-red); }
  .cover-subtitle .highlight-lead { font-size: 33px; }
  .cover-art {
    position: absolute;
    left: 123px;
    top: 497px;
    width: 373px;
    height: 347px;
    border-radius: 46% 46% 40% 40%;
    background:
      radial-gradient(ellipse at 50% 60%, #e79a98 0%, #d97b80 40%, rgba(217,123,128,0) 70%),
      linear-gradient(100deg, #2f86cf 0%, #c51d3a 45%, #e8a6a3 70%, #2f86cf 100%);
    opacity: 0.85;
  }
  .author-band {
    position: absolute;
    left: 0;
    bottom: 0;
    width: 614px;
    height: 67px;
    background: var(--band-red);
    display: flex;
    align-items: center;
    justify-content: center;
    font-family: "Open Sans", sans-serif;
    font-weight: 700;
    font-size: 27px;
    letter-spacing: 1px;
    color: var(--band-text);
  }
</style>
</head>
<body>
  <main class="book-cover">
    <svg class="cover-title" viewBox="0 0 614 330" role="heading" aria-level="1" aria-label="The Hidden Roots of Lingering Illness Decoded">
      <line class="title-rule" x1="41" y1="62" x2="218" y2="62"/>
      <line class="title-rule" x1="396" y1="62" x2="573" y2="62"/>
      <text class="title-lead" x="307" y="78" text-anchor="middle" font-size="44">THE</text>
      <text class="title-blue" x="41" y="140" font-size="74" textLength="532" lengthAdjust="spacingAndGlyphs">HIDDEN ROOTS OF</text>
      <text class="title-red" x="41" y="239" font-size="128" textLength="532" lengthAdjust="spacingAndGlyphs">LINGERING</text>
      <text class="title-blue" x="41" y="310" font-size="80" textLength="532" lengthAdjust="spacingAndGlyphs">ILLNESS</text>
    </svg>
    <svg class="cover-title" style="top:320px;height:70px" viewBox="0 0 614 70" aria-hidden="true">
      <text class="title-red" x="41" y="60" font-size="88" textLength="532" lengthAdjust="spacingAndGlyphs" style="font-family:'Montserrat',sans-serif;font-weight:900">DECODED</text>
    </svg>
    <p class="cover-subtitle">
      <span class="highlight highlight-lead">At last,</span> uncover what drives<br>
      your <span class="highlight">aches, exhaustion</span>, and<br>
      <span class="highlight">swelling.</span>
    </p>
    <div class="cover-art" role="img" aria-label="Illustration of a large anatomical heart flanked by two cartoon doctors in white coats"></div>
    <footer class="author-band">DR LENA MARSH, ND</footer>
  </main>
</body>
</html>
```